FLYER: Lighting Geometry at Rural Junctions - Review of Signage Placement - training

We are hosting a class in Australia 30, November to 4, December 2020. I would like to have a flyer designed to "sell" the class with description of course topics. I have uploaded a flyer I started on my own but I want it to be professional. Dr. Brenlow only gets to AU every 3-5 years to teach from the US. I would like to have some type of roadway scenery, prefer a nighttime scene.

Target Market(s)

Accident reconstructionists and engineers, police reconstructionists.

Font styles to use
Serif

Colors
fec214

Requirements
Must have
• Name of course and course topics, location of course, price, website and contact information.
Nice to have
• Some type of roadway background, possibly a nighttime scene on a roadway.

```html
<!DOCTYPE html>
<html lang="en">
<head>
<meta charset="utf-8">
<title>Lighting Geometry at Rural Junctions – Open Class Flyer</title>
<link rel="stylesheet" href="https://fonts.googleapis.com/css2?family=Oswald:wght@500;600;700&family=Roboto+Condensed:wght@400;700&display=swap">
<style>
  :root {
    --gold: #fec214;
    --red: #e8141b;
    --ink: #141414;
    --white: #ffffff;
    --cream: #fff8ec;
    --amber: #e88a1c;
    --ember: #7a3808;
  }
  * { margin: 0; padding: 0; box-sizing: border-box; }
  html, body { width: 1200px; height: 1200px; overflow: hidden; background: var(--white); }
  .flyer {
    position: absolute; left: 190px; top: 20px; width: 820px; height: 1160px;
    overflow: hidden; background: var(--ink);
    font-family: "Roboto Condensed", "Arial Narrow", sans-serif;
  }
  .scene-photo {
    position: absolute; inset: 0;
    background:
      radial-gradient(ellipse 60% 30% at 20% 62%, rgba(255,240,200,.55), transparent 70%),
      radial-gradient(ellipse 70% 25% at 75% 45%, rgba(255,170,60,.35), transparent 70%),
      linear-gradient(180deg, #050403 0%, #0d0805 24%, #3a1d08 36%, var(--ember) 46%, #b8620f 56%, var(--amber) 66%, #f3b865 76%, #fbe2bd 84%, var(--cream) 92%, var(--white) 100%);
  }
  .abs { position: absolute; }
  .center { left: 0; right: 0; text-align: center; }
  .display { font-family: "Oswald", "Arial Narrow", sans-serif; font-weight: 700; text-transform: uppercase; line-height: 1; }
  .title-main { top: 60px; font-size: 62px; color: var(--gold); letter-spacing: -.5px; }
  .title-sub { top: 136px; font-size: 37px; color: var(--red); line-height: 1.3; }
  .class-badge {
    top: 236px; left: 146px; width: 528px; height: 56px; background: var(--white);
    display: flex; align-items: center; justify-content: center;
    font-size: 36px; font-weight: 600; color: var(--ink);
  }
  .presenter-intro { top: 336px; font-family: "Oswald", sans-serif; font-weight: 500; font-size: 30px; color: var(--gold); }
  .presenter-name { top: 375px; font-size: 46px; color: var(--gold); }
  .presenter-name small { font-size: 32px; }
  .presenter-title { top: 422px; font-family: "Oswald", sans-serif; font-weight: 500; font-size: 22px; color: var(--gold); }
  .topics-heading { top: 462px; font-size: 44px; color: var(--red); }
  .topics-short { top: 520px; right: 463px; width: 320px; text-align: right; list-style: none; color: var(--white); font-size: 19px; line-height: 1.2; }
  .topics-short li { margin-bottom: 13px; }
  .topics-long { top: 520px; left: 399px; width: 370px; list-style: none; color: var(--white); font-size: 19px; line-height: 1.22; }
  .topics-long li { margin-bottom: 13px; }
  .fee-band {
    top: 818px; left: 0; width: 380px; height: 54px;
    background: linear-gradient(90deg, rgba(255,255,255,0) 0%, rgba(255,255,255,.9) 18%, rgba(255,255,255,.9) 82%, rgba(255,255,255,0) 100%);
    display: flex; align-items: center; justify-content: center;
    font-size: 40px; color: var(--red); padding-left: 88px;
  }
  .fee-prices { top: 878px; left: 36px; font-size: 38px; color: var(--ink); word-spacing: 18px; }
  .fee-note { top: 934px; left: 38px; width: 400px; font-size: 19px; line-height: 1.3; color: #2a2a2a; }
  .company-name { top: 1020px; left: 30px; font-size: 50px; color: var(--ink); line-height: 1.05; }
  .location { top: 838px; right: 38px; text-align: right; color: var(--ink); }
  .location-heading { font-family: "Oswald", sans-serif; font-weight: 600; font-size: 30px; display: flex; align-items: flex-end; justify-content: flex-end; gap: 6px; }
  .location-address { margin-top: 10px; font-size: 18px; line-height: 1.3; margin-right: 10px; }
  .contact { top: 964px; left: 488px; width: 294px; border-top: 1px solid #b9b0a5; padding-top: 8px; text-align: right; color: var(--ink); }
  .contact-lead { font-size: 30px; line-height: 1.1; }
  .contact-web { font-size: 21px; font-weight: 700; margin-top: 2px; }
  .contact-or { font-size: 21px; margin-top: 4px; }
  .contact-email { font-size: 22px; }
  .contact-phone { font-family: "Oswald", sans-serif; font-weight: 700; font-size: 50px; line-height: 1.1; }
</style>
</head>
<body>
<main class="flyer">
  <div class="scene-photo" role="img" aria-label="Long-exposure night photograph of a city roadway with amber light trails and street lamps"></div>

  <h1 class="abs center display title-main">Lighting Geometry</h1>
  <h2 class="abs center display title-sub">At Rural Junctions, Review<br>of Signage Placement</h2>
  <div class="abs display class-badge">Open Class:&nbsp;&nbsp;Manley NSW</div>

  <p class="abs center presenter-intro">Presented by</p>
  <p class="abs center display presenter-name">Adrian Brenlow <small>Ph.D.</small></p>
  <p class="abs center presenter-title">WORLD RENOWNED HUMAN FACTORS EXPERT</p>

  <h3 class="abs center display topics-heading">Course Topics</h3>
  <ul class="abs topics-short">
    <li>Acceleration</li>
    <li>Research in IDRR</li>
    <li>Nighttime recognition</li>
    <li>Driver decision making</li>
    <li>Perception-Response Time</li>
    <li>Pedestrian walking speeds</li>
    <li>Headlight mapping demonstration and instruction</li>
  </ul>
  <ul class="abs topics-long">
    <li>Response to slow moving or stopped vehicles on multilane high speed roads</li>
    <li>Lateral acceleration (swerving) for cars, motorcycles, and commercial vehicles</li>
    <li>Forward and backward acceleration of cars, motorcycles and commercial vehicles</li>
    <li>Gap acceptance for left turns, right turns, and through movements for drivers, riders, and pedestrians</li>
    <li>Drivers’ responses to green and yellow traffic signals, deceleration choice, reaction time and probability of stopping</li>
  </ul>

  <div class="abs display fee-band">Course Fee</div>
  <p class="abs display fee-prices">$1,730&nbsp;AU $1,200&nbsp;USD</p>
  <p class="abs fee-note">It has been 3 years since Dr. Brenlow has come to AU to teach, don’t miss out on this year’s class.</p>

  <p class="abs display company-name">Roadline<br>Safety Group</p>

  <div class="abs location">
    <div class="location-heading">
      Location
      <svg width="38" height="76" viewBox="0 0 38 76" aria-hidden="true">
        <path d="M19 2 C9 2 2 9 2 19 C2 33 19 74 19 74 C19 74 36 33 36 19 C36 9 29 2 19 2 Z" fill="#141414"/>
        <circle cx="19" cy="19" r="9" fill="#f6d9ad"/>
      </svg>
    </div>
    <p class="location-address">Keelbay Lodge – Sydney Harbor National Park<br>12 Headland Lookout Road, Manley NSW</p>
  </div>

  <div class="abs contact">
    <p class="contact-lead">Register on our website</p>
    <p class="contact-web">www.roadlinesafetygroup.com</p>
    <p class="contact-or">or Contact:</p>
    <p class="contact-email">Tessa@roadlinesafetygroup.com</p>
    <p class="contact-phone">555-204-7731</p>
  </div>
</main>
</body>
</html>
```